Design for iOS app - Scanner App

We are developing an iOS app that is scanning receipts and mailing them to a predefined email address. The app should work more or less like TallySnap app (a short demo of the TallySnap app is available here: https://www.vidloomer.com/watch?v=QpRtWx83LmK).

We have prototyped the app in the link below:
http://app.framewisp.com/view/a71c3d02b58e9f46c1d7e0a2b94f8c5d

NB!: Please do not follow the mockups literally, but the Velmor Touch Layout Handbook!

The technical specifications and descriptions of the app's functionalities are available in the link below:
https://sheets.pallowdocs.com/document/d/7mPqo-RZ2xLwQbTfHaVk9YeNuJsDcX_3Pgtn4Hmcz5/edit?usp=sharing

Requirements for the design:

- The design should be provided as PSD, where each page/section should be in its own PSD file OR all pages/sections should be represented as folder groups in a single PSD file.

- All graphical elements in the design should be delivered as single layers which can then be extracted from the PSD.

- All graphical elements (icons, graphical buttons, etc.) should be provided as vector objects in the PSD, so that they can be exported into different sizes without loss of quality (for responsiveness).

- The design should use either web safe fonts or Google Fonts.

Instructions for the design:

The design should have habitual user interface like ordinary iOS navigation stack, with navigation bar on the top and all other elements on the bottom. That means just to make the top bar in your app be more like iOS. Please follow the Velmor Touch Layout Handbook, not the mockups literally .
FX: the e small elements in Dimensions screen like delete icons and active checkbox. In
https://devs.quorrelfield.com/library/mobile/documentation/UserExperience/Conceptual/TouchGuide/LayoutandAppearance.html#//ref/doc/uid/TX50017283-CH21-SW1
is described that interface elements should be at least 44x44 px - it's normal practice for all mobile development (iOS, android), so you should consider this too.

Please also provide an app icon and suggest a logo for the app.

Requirements
Must have
• Please make sure that the design is flat. Like iOS app, Pagelift, Tessivo apps etc.
Nice to have
• The design could be somewhat like the design for Brindlemark Pagelift(https://apps.quorrelstore.com/bg/app/brindlemark-pagelift/id451927730?mt=8) without being too similar
Should not have
• 3D look

```html
<!DOCTYPE html>
<html lang="en">
<head>
<meta charset="utf-8">
<title>SKANO – receipt scanner app screens</title>
<link href="https://fonts.googleapis.com/css2?family=Open+Sans:wght@400;600;700;800&display=swap" rel="stylesheet">
<style>
:root{
  --red:#e8493c;
  --red-dark:#c93a2f;
  --blue:#45bdf0;
  --blue-dark:#2d9fd3;
  --teal:#1dbd9a;
  --teal-dark:#159c7f;
  --stage:#2e2e2e;
  --stage-light:#3a3a3a;
  --panel:#e9e9e9;
  --head:#dedede;
  --field:#eeeeee;
  --line:#d6d6d6;
  --ink:#444;
  --muted:#9a9a9a;
  --white:#fff;
  --caption:#e6e6e6;
}
*{box-sizing:border-box;margin:0;padding:0}
html,body{width:1200px;height:2535px;overflow:hidden}
body{font-family:"Open Sans",Arial,sans-serif;background:var(--stage)}
.stage{position:relative;width:1200px;height:2535px;overflow:hidden;
  background:radial-gradient(ellipse at 50% 30%,var(--stage-light),var(--stage) 70%)}
.ribbon{position:absolute;width:460px;height:96px;left:870px;top:40px;transform:rotate(45deg);
  background:var(--red);color:var(--white);font-weight:700;font-size:27px;line-height:32px;
  display:flex;flex-direction:column;align-items:center;justify-content:center;text-align:center}
.board{position:absolute;left:69px;top:133px;display:grid;
  grid-template-columns:repeat(4,200px);grid-auto-rows:621px;column-gap:76px}
.cell{display:flex;flex-direction:column;align-items:center}
.caption{margin-top:86px;color:var(--caption);font-size:19px}
.screen{position:relative;width:200px;height:410px;background:var(--white);overflow:hidden;
  display:flex;flex-direction:column;border-radius:4px;font-size:9px;color:var(--ink)}
.nav{height:30px;flex:none;background:var(--red);display:flex;align-items:center;
  justify-content:space-between;padding:0 8px;color:var(--white)}
.nav .brand{position:absolute;left:0;right:0;text-align:center;font-weight:800;font-size:14px;letter-spacing:.5px;pointer-events:none}
.nav .tools{display:flex;gap:7px}
.nav svg{display:block}
.section-head{height:22px;flex:none;background:var(--head);display:flex;align-items:center;gap:5px;
  padding:0 8px;font-weight:700;font-size:9px}
.body{flex:1;position:relative;background:var(--white)}
.foot{flex:none;background:var(--panel);padding:5px 0 40px}
.btn{height:21px;margin:0 8px 5px;display:flex;align-items:center;justify-content:center;
  color:var(--white);font-size:9px;font-weight:600}
.btn.red{background:var(--red)}.btn.blue{background:var(--blue)}.btn.teal{background:var(--teal)}
/* main */
.start{position:absolute;left:50px;top:76px;width:100px;height:100px;border-radius:50%;
  background:var(--red);box-shadow:0 0 0 6px #f6c9c4;color:var(--white);font-weight:700;
  font-size:11px;line-height:13px;display:flex;align-items:center;justify-content:center;text-align:center}
.status{position:absolute;left:0;right:0;top:250px;text-align:center;font-size:7px;color:var(--muted);letter-spacing:.5px}
.counters{position:absolute;left:0;right:0;top:280px}
.counter{height:21px;display:flex;align-items:center;justify-content:space-between;color:var(--white);font-size:9px;padding-left:8px;margin-bottom:2px}
.counter b{width:34px;height:100%;display:flex;align-items:center;justify-content:center;font-weight:700}
.counter.pending{background:var(--blue)}.counter.pending b{background:var(--blue-dark)}
.counter.sent{background:var(--teal)}.counter.sent b{background:var(--teal-dark)}
.tray{position:absolute;left:0;right:0;bottom:0;height:34px;background:var(--panel)}
.faded{opacity:.25}
.modal{position:absolute;left:0;right:0;top:84px;text-align:center;padding:0 14px;font-size:8.5px;line-height:12px}
.modal .hl{color:var(--red);font-weight:700}
.modal .btn{margin:12px -6px 0}
.modal .btn+.btn{margin-top:5px}
/* splash */
.splash{background:linear-gradient(160deg,#ec5a4d,var(--red) 55%,#d9473b)}
.splash-photo{position:absolute;inset:0;background:linear-gradient(200deg,rgba(255,255,255,.08),rgba(0,0,0,.1))}
.splash-mark{position:absolute;left:0;right:0;top:165px;display:flex;flex-direction:column;align-items:center;color:var(--white)}
.splash-mark .square{width:22px;height:26px;border:2px solid var(--white);margin-bottom:6px}
.splash-mark .name{font-weight:800;font-size:20px;letter-spacing:1px}
.splash-mark .tag{font-size:5px;letter-spacing:.5px;margin-top:2px}
/* forms */
.row{display:flex;align-items:center;justify-content:space-between;padding:0 8px;height:20px}
.row.label{font-weight:700}
.row.sub{color:var(--muted);height:14px;font-size:8px}
.check{width:11px;height:11px;border:1px solid var(--line);background:var(--white)}
.check.on{background:var(--blue);border-color:var(--blue)}
.add{display:flex;margin:4px 8px 8px;height:18px}
.add span{flex:1;background:var(--field);border:1px solid var(--line)}
.add b{width:26px;background:var(--blue);color:var(--white);font-size:7px;display:flex;align-items:center;justify-content:center}
.field-label{padding:7px 8px 3px;font-size:8.5px}
.field{margin:0 8px;height:18px;background:var(--field);border:1px solid var(--line);position:relative}
.field.select::after{content:"";position:absolute;right:6px;top:5px;width:4px;height:4px;border-right:1px solid #777;border-bottom:1px solid #777;transform:rotate(45deg)}
.field.area{height:22px}
/* receipts */
.thumbs{display:flex;flex-wrap:wrap;gap:6px;padding:10px 8px}
.thumb{width:39px;height:40px;border:2px solid #c89a6a;background:linear-gradient(180deg,#f0e9de,#d9cdbd)}
.thumb.empty{border:1px solid var(--line);background:var(--field);font-size:4.5px;color:var(--muted);display:flex;align-items:center;justify-content:center;text-align:center}
/* camera */
.camera{flex:1;background:#1d1d1d;position:relative}
.viewfinder{position:absolute;left:10px;right:10px;top:12px;bottom:8px;background:#4a4a4a;
  display:flex;align-items:center;justify-content:center;text-align:center;color:#8d8d8d;font-size:9px;line-height:12px}
.viewfinder.target{border:6px solid var(--red)}
.viewfinder.preview{border:6px solid #3a3a3a;background:#555}
.shutter{height:34px;flex:none;background:#111;display:flex;align-items:center;justify-content:space-between;padding:0 10px;color:#ddd;font-size:8px}
.shutter i{width:20px;height:20px;border-radius:50%;background:var(--red)}
/* help */
.group{background:var(--head);height:16px;display:flex;align-items:center;padding:0 8px;font-weight:700;font-size:8px}
.item{height:20px;display:flex;align-items:center;justify-content:space-between;padding:0 8px;border-bottom:1px solid #eee;font-size:8px}
.item .val{color:var(--muted)}
.item.alert{color:var(--red)}
.go{width:9px;height:9px;border-radius:50%;background:var(--red);display:flex;align-items:center;justify-content:center}
.article{padding:8px;font-size:7px;line-height:9.6px;color:#666}
</style>
</head>
<body>
<div class="stage">
  <div class="ribbon"><span>Follow The Links</span><span>for detail</span></div>

  <div class="board">

    <!-- Row 1 -->
    <div class="cell">
      <div class="screen splash">
        <div class="splash-photo" role="img" aria-label="Faint photo of a paper receipt behind the red splash colour"></div>
        <div class="splash-mark">
          <div class="square"></div>
          <div class="name">SKANO</div>
          <div class="tag">YOUR RECEIPT SCANNING APP</div>
        </div>
      </div>
      <div class="caption">Splash</div>
    </div>

    <div class="cell">
      <div class="screen">
        <div class="nav">
          <svg width="11" height="11" viewBox="0 0 11 11"><circle cx="5.5" cy="5.5" r="5" fill="#fff"/><path d="M5.5 4.5v4M5.5 2.5v1" stroke="#e8493c" stroke-width="1.4"/></svg>
          <span class="brand">SKANO</span>
          <span class="tools">
            <svg width="11" height="10" viewBox="0 0 11 10"><path d="M0 1h2M4 1h7M0 5h2M4 5h7M0 9h2M4 9h7" stroke="#fff" stroke-width="1.5"/></svg>
            <svg width="10" height="10" viewBox="0 0 10 10"><circle cx="5" cy="5" r="3.3" fill="none" stroke="#fff" stroke-width="2.4" stroke-dasharray="1.6 1"/><circle cx="5" cy="5" r="1.3" fill="#fff"/></svg>
          </span>
        </div>
        <div class="body">
          <div class="start">START<br>SCANNING</div>
          <div class="status">READY</div>
          <div class="counters">
            <div class="counter pending">Pending<b>12</b></div>
            <div class="counter sent">Sent<b>3</b></div>
          </div>
          <div class="tray"></div>
        </div>
      </div>
      <div class="caption">Main Screen</div>
    </div>

    <div class="cell">
      <div class="screen">
        <div class="nav">
          <svg width="11" height="11" viewBox="0 0 11 11"><circle cx="5.5" cy="5.5" r="5" fill="#fff"/><path d="M5.5 4.5v4M5.5 2.5v1" stroke="#e8493c" stroke-width="1.4"/></svg>
          <span class="brand">SKANO</span>
          <span class="tools">
            <svg width="11" height="10" viewBox="0 0 11 10"><path d="M0 1h2M4 1h7M0 5h2M4 5h7M0 9h2M4 9h7" stroke="#fff" stroke-width="1.5"/></svg>
            <svg width="10" height="10" viewBox="0 0 10 10"><circle cx="5" cy="5" r="3.3" fill="none" stroke="#fff" stroke-width="2.4" stroke-dasharray="1.6 1"/><circle cx="5" cy="5" r="1.3" fill="#fff"/></svg>
          </span>
        </div>
        <div class="body">
          <div class="counters faded">
            <div class="counter pending">Pending<b>12</b></div>
            <div class="counter sent">Sent<b>3</b></div>
          </div>
          <div class="tray faded"></div>
          <div class="modal" style="top:100px">
            <p><b>Your <span class="hl">14-Days Trial</span> period<br>has expired.</b></p>
            <p style="margin-top:8px"><b>Please <span class="hl">subscribe</span> for the app<br>if you would like to using it</b></p>
            <div class="btn red">Subscribe</div>
          </div>
        </div>
      </div>
      <div class="caption">Main Trial Exp</div>
    </div>

    <div class="cell">
      <div class="screen">
        <div class="nav">
          <svg width="11" height="11" viewBox="0 0 11 11"><circle cx="5.5" cy="5.5" r="5" fill="#fff"/><path d="M5.5 4.5v4M5.5 2.5v1" stroke="#e8493c" stroke-width="1.4"/></svg>
          <span class="brand">SKANO</span>
          <span class="tools">
            <svg width="11" height="10" viewBox="0 0 11 10"><path d="M0 1h2M4 1h7M0 5h2M4 5h7M0 9h2M4 9h7" stroke="#fff" stroke-width="1.5"/></svg>
            <svg width="10" height="10" viewBox="0 0 10 10"><circle cx="5" cy="5" r="3.3" fill="none" stroke="#fff" stroke-width="2.4" stroke-dasharray="1.6 1"/><circle cx="5" cy="5" r="1.3" fill="#fff"/></svg>
          </span>
        </div>
        <div class="body">
          <div class="counters faded">
            <div class="counter pending">Pending<b>12</b></div>
            <div class="counter sent">Sent<b>3</b></div>
          </div>
          <div class="tray faded"></div>
          <div class="modal" style="top:70px">
            <p class="hl">Confirm your subscription</p>
            <p style="margin-top:6px">Do you want to subscribe to<br><span class="hl">SKANO</span> ( 1 Year ) for $4.99?</p>
            <p style="margin-top:6px">This subscription will automatically<br>renew until canceled.</p>
            <div class="btn red">Cancel</div>
            <div class="btn blue">Confirm</div>
          </div>
        </div>
      </div>
      <div class="caption">Main Confirm Sub</div>
    </div>

    <!-- Row 2 -->
    <div class="cell">
      <div class="screen">
        <div class="nav">
          <svg width="11" height="11" viewBox="0 0 11 11"><circle cx="5.5" cy="5.5" r="5" fill="#fff"/><path d="M5.5 4.5v4M5.5 2.5v1" stroke="#e8493c" stroke-width="1.4"/></svg>
          <span class="brand">SKANO</span>
          <span class="tools">
            <svg width="11" height="10" viewBox="0 0 11 10"><path d="M0 1h2M4 1h7M0 5h2M4 5h7M0 9h2M4 9h7" stroke="#fff" stroke-width="1.5"/></svg>
            <svg width="10" height="10" viewBox="0 0 10 10"><circle cx="5" cy="5" r="3.3" fill="none" stroke="#fff" stroke-width="2.4" stroke-dasharray="1.6 1"/><circle cx="5" cy="5" r="1.3" fill="#fff"/></svg>
          </span>
        </div>
        <div class="body">
          <div class="counters faded">
            <div class="counter pending">Pending<b>12</b></div>
            <div class="counter sent">Sent<b>3</b></div>
          </div>
          <div class="tray faded"></div>
          <div class="modal" style="top:88px">
            <p class="hl">Thank you for subscribing</p>
            <p>Your purchase was successful<br>to go the Quorrel Store and Review<br>subscription settings or cancel<br>auto-renewal, Tap Manage.</p>
            <div class="btn red" style="margin-top:18px">Manage</div>
            <div class="btn blue">OK</div>
          </div>
        </div>
      </div>
      <div class="caption">Main Thank you</div>
    </div>

    <div class="cell">
      <div class="screen">
        <div class="nav">
          <svg width="8" height="12" viewBox="0 0 8 12"><path d="M6.5 1L1.5 6l5 5" fill="none" stroke="#fff" stroke-width="2"/></svg>
          <span class="brand">SKANO</span><span></span>
        </div>
        <div class="section-head">
          <svg width="9" height="8" viewBox="0 0 9 8"><path d="M0 1h9M0 4h9M0 7h9" stroke="#444" stroke-width="1.3"/></svg>Dimensions
        </div>
        <div class="body">
          <div class="row label" style="margin-top:6px"><span>Daily cost <span style="color:var(--red)">✎</span></span><span style="display:flex;gap:5px;align-items:center">Active <i class="check on"></i></span></div>
          <div class="row sub"><span>Drink</span><span>—</span></div>
          <div class="row sub"><span>Snack</span><span>—</span></div>
          <div class="add"><span></span><b>ADD</b></div>
          <div class="row label"><span>Payment <span style="color:var(--red)">✎</span></span><span style="display:flex;gap:5px;align-items:center">Active <i class="check"></i></span></div>
          <div class="add"><span></span><b>ADD</b></div>
        </div>
        <div class="foot">
          <div class="btn teal">Save</div>
          <div class="btn blue">Close</div>
        </div>
      </div>
      <div class="caption">Dimension</div>
    </div>

    <div class="cell">
      <div class="screen">
        <div class="nav">
          <svg width="8" height="12" viewBox="0 0 8 12"><path d="M6.5 1L1.5 6l5 5" fill="none" stroke="#fff" stroke-width="2"/></svg>
          <span class="brand">SKANO</span><span></span>
        </div>
        <div class="section-head">
          <svg width="9" height="9" viewBox="0 0 10 10"><circle cx="5" cy="5" r="3.3" fill="none" stroke="#444" stroke-width="2.4" stroke-dasharray="1.6 1"/><circle cx="5" cy="5" r="1.3" fill="#444"/></svg>Settings
        </div>
        <div class="body">
          <div class="field-label">Email</div><div class="field"></div>
          <div class="field-label">CC</div><div class="field"></div>
          <div class="field-label">Name</div><div class="field"></div>
          <div class="row" style="margin-top:4px"><span>Save to Camera Roll</span><i class="check on"></i></div>
        </div>
        <div class="foot">
          <div class="btn teal">Save</div>
          <div class="btn blue">Close</div>
        </div>
      </div>
      <div class="caption">Settings</div>
    </div>

    <div class="cell">
      <div class="screen">
        <div class="nav">
          <svg width="8" height="12" viewBox="0 0 8 12"><path d="M6.5 1L1.5 6l5 5" fill="none" stroke="#fff" stroke-width="2"/></svg>
          <span class="brand">SKANO</span><span></span>
        </div>
        <div class="section-head">
          <svg width="9" height="8" viewBox="0 0 9 8"><rect x=".5" y=".5" width="8" height="7" fill="none" stroke="#444"/><path d="M2 3h5M2 5h5" stroke="#444"/></svg>Pending Receipts
        </div>
        <div class="body">
          <div class="thumbs">
            <div class="thumb" role="img" aria-label="Receipt photo thumbnail"></div>
            <div class="thumb" role="img" aria-label="Receipt photo thumbnail"></div>
            <div class="thumb" role="img" aria-label="Receipt photo thumbnail"></div>
            <div class="thumb empty">ADD<br>RECEIPT</div>
          </div>
        </div>
        <div class="foot">
          <div class="btn teal">Send All</div>
          <div class="btn red">Delete All</div>
          <div class="btn blue">Close</div>
        </div>
      </div>
      <div class="caption">Pending</div>
    </div>

    <!-- Row 3 -->
    <div class="cell">
      <div class="screen">
        <div class="nav">
          <svg width="8" height="12" viewBox="0 0 8 12"><path d="M6.5 1L1.5 6l5 5" fill="none" stroke="#fff" stroke-width="2"/></svg>
          <span class="brand">SKANO</span><span></span>
        </div>
        <div class="section-head">
          <svg width="9" height="8" viewBox="0 0 9 8"><rect x=".5" y=".5" width="8" height="7" fill="none" stroke="#444"/><path d="M2 3h5M2 5h5" stroke="#444"/></svg>Sent Receipts
        </div>
        <div class="body">
          <div class="thumbs">
            <div class="thumb" role="img" aria-label="Sent receipt photo thumbnail"></div>
            <div class="thumb" role="img" aria-label="Sent receipt photo thumbnail"></div>
            <div class="thumb" role="img" aria-label="Sent receipt photo thumbnail"></div>
          </div>
        </div>
        <div class="foot">
          <div class="btn red">Delete All</div>
          <div class="btn blue">Close</div>
        </div>
      </div>
      <div class="caption">Sent</div>
    </div>

    <div class="cell">
      <div class="screen">
        <div class="nav">
          <svg width="8" height="12" viewBox="0 0 8 12"><path d="M6.5 1L1.5 6l5 5" fill="none" stroke="#fff" stroke-width="2"/></svg>
          <span class="brand">SKANO</span><span></span>
        </div>
        <div class="camera"><div class="viewfinder target">RECEIPT<br>IMAGE<br>TO SCAN</div></div>
        <div class="shutter"><span>Cancel</span><i></i><span>From Photos</span></div>
      </div>
      <div class="caption">Scan</div>
    </div>

    <div class="cell">
      <div class="screen">
        <div class="nav">
          <svg width="8" height="12" viewBox="0 0 8 12"><path d="M6.5 1L1.5 6l5 5" fill="none" stroke="#fff" stroke-width="2"/></svg>
          <span class="brand">SKANO</span><span></span>
        </div>
        <div class="camera"><div class="viewfinder preview">Preview<br>Scan</div></div>
        <div class="shutter"><span>Retake</span><span>Continue</span></div>
      </div>
      <div class="caption">Scan Preview</div>
    </div>

    <div class="cell">
      <div class="screen">
        <div class="nav">
          <svg width="8" height="12" viewBox="0 0 8 12"><path d="M6.5 1L1.5 6l5 5" fill="none" stroke="#fff" stroke-width="2"/></svg>
          <span class="brand">SKANO</span><span></span>
        </div>
        <div class="section-head">
          <svg width="9" height="9" viewBox="0 0 10 10"><circle cx="5" cy="5" r="3.3" fill="none" stroke="#444" stroke-width="2.4" stroke-dasharray="1.6 1"/><circle cx="5" cy="5" r="1.3" fill="#444"/></svg>Settings
        </div>
        <div class="body">
          <div class="field-label">Type of cost</div><div class="field select"></div>
          <div class="field-label">Payment Method</div><div class="field select"></div>
          <div class="field-label">Dimension</div><div class="field select"></div>
          <div class="field-label">Description</div><div class="field area"></div>
        </div>
        <div class="foot">
          <div class="btn teal">Send</div>
          <div class="btn blue">Cancel</div>
        </div>
      </div>
      <div class="caption">Scan Upload</div>
    </div>

    <!-- Row 4 -->
    <div class="cell">
      <div class="screen">
        <div class="nav">
          <svg width="11" height="11" viewBox="0 0 11 11"><circle cx="5.5" cy="5.5" r="5" fill="#fff"/><path d="M5.5 4.5v4M5.5 2.5v1" stroke="#e8493c" stroke-width="1.4"/></svg>
          <span class="brand">SKANO</span>
          <span class="tools">
            <svg width="11" height="10" viewBox="0 0 11 10"><path d="M0 1h2M4 1h7M0 5h2M4 5h7M0 9h2M4 9h7" stroke="#fff" stroke-width="1.5"/></svg>
            <svg width="10" height="10" viewBox="0 0 10 10"><circle cx="5" cy="5" r="3.3" fill="none" stroke="#fff" stroke-width="2.4" stroke-dasharray="1.6 1"/><circle cx="5" cy="5" r="1.3" fill="#fff"/></svg>
          </span>
        </div>
        <div class="body">
          <div class="start">START<br>SCANNING</div>
          <div class="status">UPLOADED</div>
          <div class="counters">
            <div class="counter pending">Pending<b>12</b></div>
            <div class="counter sent">Sent<b>3</b></div>
          </div>
          <div class="tray"></div>
        </div>
      </div>
      <div class="caption">Upload Complete</div>
    </div>

    <div class="cell">
      <div class="screen">
        <div class="nav">
          <svg width="8" height="12" viewBox="0 0 8 12"><path d="M6.5 1L1.5 6l5 5" fill="none" stroke="#fff" stroke-width="2"/></svg>
          <span class="brand">SKANO</span><span></span>
        </div>
        <div class="section-head">
          <svg width="9" height="9" viewBox="0 0 10 10"><circle cx="5" cy="5" r="4.5" fill="#444"/><path d="M3.6 3.8a1.5 1.5 0 1 1 1.4 2V6.6M5 7.6v.8" fill="none" stroke="#fff" stroke-width="1"/></svg>Help
        </div>
        <div class="body">
          <div class="group">Account</div>
          <div class="item"><span>Email</span><span class="val">lena@tallymail.com</span></div>
          <div class="item"><span>SkanoApp</span><span class="val">Trial</span></div>
          <div class="item alert"><span>Upgrade Now!</span><i class="go"><svg width="4" height="5" viewBox="0 0 4 5"><path d="M1 .5l2 2-2 2" fill="none" stroke="#fff"/></svg></i></div>
          <div class="group">More</div>
          <div class="item"><span>About</span><i class="go"><svg width="4" height="5" viewBox="0 0 4 5"><path d="M1 .5l2 2-2 2" fill="none" stroke="#fff"/></svg></i></div>
          <div class="item"><span>Privacy Policy</span><i class="go"><svg width="4" height="5" viewBox="0 0 4 5"><path d="M1 .5l2 2-2 2" fill="none" stroke="#fff"/></svg></i></div>
          <div class="item"><span>Support</span><i class="go"><svg width="4" height="5" viewBox="0 0 4 5"><path d="M1 .5l2 2-2 2" fill="none" stroke="#fff"/></svg></i></div>
          <div class="item"><span>Feedback</span><i class="go"><svg width="4" height="5" viewBox="0 0 4 5"><path d="M1 .5l2 2-2 2" fill="none" stroke="#fff"/></svg></i></div>
        </div>
      </div>
      <div class="caption">Help</div>
    </div>

    <div class="cell">
      <div class="screen">
        <div class="nav">
          <svg width="8" height="12" viewBox="0 0 8 12"><path d="M6.5 1L1.5 6l5 5" fill="none" stroke="#fff" stroke-width="2"/></svg>
          <span class="brand">SKANO</span><span></span>
        </div>
        <div class="section-head">
          <svg width="9" height="9" viewBox="0 0 10 10"><circle cx="5" cy="5" r="4.5" fill="#444"/><path d="M3.6 3.8a1.5 1.5 0 1 1 1.4 2V6.6M5 7.6v.8" fill="none" stroke="#fff" stroke-width="1"/></svg>Help
        </div>
        <div class="body">
          <div class="group">Account</div>
          <div class="item"><span>Email</span><span class="val">lena@tallymail.com</span></div>
          <div class="item"><span>Manage Your Subscription</span><i class="go"><svg width="4" height="5" viewBox="0 0 4 5"><path d="M1 .5l2 2-2 2" fill="none" stroke="#fff"/></svg></i></div>
          <div class="group">More</div>
          <div class="item"><span>About</span><i class="go"><svg width="4" height="5" viewBox="0 0 4 5"><path d="M1 .5l2 2-2 2" fill="none" stroke="#fff"/></svg></i></div>
          <div class="item"><span>Privacy Policy</span><i class="go"><svg width="4" height="5" viewBox="0 0 4 5"><path d="M1 .5l2 2-2 2" fill="none" stroke="#fff"/></svg></i></div>
          <div class="item"><span>Support</span><i class="go"><svg width="4" height="5" viewBox="0 0 4 5"><path d="M1 .5l2 2-2 2" fill="none" stroke="#fff"/></svg></i></div>
          <div class="item"><span>Feedback</span><i class="go"><svg width="4" height="5" viewBox="0 0 4 5"><path d="M1 .5l2 2-2 2" fill="none" stroke="#fff"/></svg></i></div>
        </div>
      </div>
      <div class="caption">Help Subscription</div>
    </div>

    <div class="cell">
      <div class="screen">
        <div class="nav">
          <svg width="8" height="12" viewBox="0 0 8 12"><path d="M6.5 1L1.5 6l5 5" fill="none" stroke="#fff" stroke-width="2"/></svg>
          <span class="brand">SKANO</span><span></span>
        </div>
        <div class="section-head">
          <svg width="9" height="9" viewBox="0 0 10 10"><circle cx="5" cy="5" r="4.5" fill="#444"/><path d="M3.6 3.8a1.5 1.5 0 1 1 1.4 2V6.6M5 7.6v.8" fill="none" stroke="#fff" stroke-width="1"/></svg>Help
        </div>
        <div class="body">
          <p class="article">Lorem ipsum dolor sit amet, consectetuer adipiscing elit, sed diam nonummy nibh euismod tincidunt ut laoreet dolore magna aliquam erat volutpat. Ut wisi enim ad minim veniam, quis nostrud exerci tation ullamcorper suscipit lobortis nisl ut aliquip ex ea commodo consequat. Duis autem vel eum iriure dolor in hendrerit in vulputate velit esse molestie consequat, vel illum dolore eu feugiat nulla facilisis at vero eros et accumsan et iusto odio dignissim qui blandit praesent luptatum zzril delenit augue duis dolore te feugait nulla facilisi. Nam liber tempor cum soluta nobis eleifend option congue nihil imperdiet doming id quod mazim placerat facer possim assum.</p>
        </div>
        <div class="foot">
          <div class="btn blue">Close</div>
        </div>
      </div>
      <div class="caption">Help Article</div>
    </div>

  </div>
</div>
</body>
</html>
```